Remote Planning & Scheduling Power Point Presentation

This PP presentation is to help explain what RPS is and its benefits. Need help with a better illustration on slide 3 that explains the process, overall aesthetics, need better images, and cleaner workflow on slide 18. Keep the DEW Logo in the bottom right of each slide. I have included a one-pager and infographic to help. I am still working of verbiage.

Thanks
SL

```html
<!DOCTYPE html>
<html lang="en">
<head>
<meta charset="utf-8">
<title>Remote Planning &amp; Scheduling – DEW</title>
<link href="https://fonts.googleapis.com/css2?family=Didact+Gothic&family=Catamaran:wght@600;700&display=swap" rel="stylesheet">
<style>
  :root {
    --page: #e8e5e0;
    --navy: #0f2f9e;
    --navy-deep: #0b2380;
    --steel: #4b5565;
    --white: #ffffff;
    --body-text: #5a5f66;
    --bullet: #1338a8;
    --sky: #28a4e4;
    --azure: #1c72e0;
    --orange: #f7941d;
    --amber: #fbb040;
    --mark-grey: #c9ccd3;
  }
  * { box-sizing: border-box; margin: 0; padding: 0; }
  html, body { width: 1200px; height: 752px; overflow: hidden; }
  body {
    background: var(--page);
    font-family: "Didact Gothic", "Century Gothic", sans-serif;
    position: relative;
  }
  .slide {
    position: absolute;
    width: 559px;
    height: 315px;
    overflow: hidden;
    background: var(--white);
    box-shadow: 0 2px 6px rgba(0,0,0,.18);
  }
  .slide--cover { left: 26px; top: 35px; background: var(--navy); }
  .slide--approach { left: 616px; top: 35px; }
  .slide--detail { left: 26px; top: 378px; }
  .slide--flow { left: 616px; top: 378px; }
  .slide-frame { position: absolute; inset: 0; width: 100%; height: 100%; }

  .cover-photo {
    position: absolute; inset: 0;
    background: linear-gradient(180deg, #1440b0 0%, #1a3fa6 45%, #163794 75%, #1c3c98 100%);
  }
  .cover-title {
    position: absolute; top: 58px; left: 0; width: 100%;
    text-align: center; color: var(--white); font-size: 17px; letter-spacing: .5px;
  }
  .cover-brand {
    position: absolute; top: 146px; left: 0; width: 100%;
    text-align: center; color: var(--white);
    font-family: "Catamaran", sans-serif; font-weight: 700; font-size: 42px; letter-spacing: 2px;
  }
  .cover-year {
    position: absolute; top: 256px; left: 0; width: 100%;
    text-align: center; color: var(--white); font-size: 9px;
  }
  .corner-mark {
    position: absolute; right: 22px; bottom: 17px;
    font-family: "Catamaran", sans-serif; font-weight: 700; font-size: 14px;
    color: var(--mark-grey); letter-spacing: .5px;
  }
  .slide--cover .corner-mark { color: rgba(255,255,255,.35); right: 40px; bottom: 38px; }
  .slide--flow .corner-mark { color: rgba(255,255,255,.18); }

  .slide-title {
    position: absolute; left: 44px; top: 38px;
    color: var(--white); font-size: 21px; letter-spacing: .3px;
  }
  .slide--flow .slide-title { left: 40px; top: 11px; color: var(--navy); font-size: 20px; }

  .bullet-list { position: absolute; list-style: none; color: var(--body-text); font-size: 11.5px; line-height: 14px; }
  .bullet-list li { position: relative; padding-left: 18px; }
  .bullet-list li::before {
    content: ""; position: absolute; left: 0; top: 3px;
    border-left: 7px solid var(--bullet);
    border-top: 4px solid transparent; border-bottom: 4px solid transparent;
  }
  .benefits { top: 179px; display: flex; width: 100%; }
  .benefits li { position: absolute; text-align: center; font-size: 12px; }
  .benefits li:nth-child(1) { left: 48px; width: 200px; }
  .benefits li:nth-child(2) { left: 268px; width: 268px; }
  .benefits li::before { top: 4px; }

  .steps-field { left: 49px; top: 138px; width: 200px; }
  .steps-field li { margin-bottom: 14px; }
  .steps-office { left: 268px; top: 130px; width: 290px; }
  .steps-office li { margin-bottom: 4.6px; }

  .flow-label { font-family: "Catamaran", sans-serif; font-weight: 700; font-size: 6.4px; }
  .flow-label--light { fill: var(--white); }
  .flow-label--dark { fill: #17307c; }
  .hub-label { font-family: "Catamaran", sans-serif; font-weight: 600; font-size: 8.5px; }
</style>
</head>
<body>

<!-- Cover -->
<section class="slide slide--cover">
  <div class="cover-photo" role="img" aria-label="Refinery skyline photo in deep blue tones"></div>
  <h1 class="cover-title">Remote Planning &amp; Scheduling</h1>
  <div class="cover-brand">DEW</div>
  <div class="cover-year">2020</div>
  <div class="corner-mark">DEW</div>
</section>

<!-- Benefits -->
<section class="slide slide--approach">
  <svg class="slide-frame" viewBox="0 0 559 315" aria-hidden="true">
    <polygon points="0,0 559,0 559,136 524,89 0,89" fill="var(--navy)"/>
    <polygon points="491,0 559,0 559,91" fill="var(--steel)"/>
  </svg>
  <h2 class="slide-title">Innovative Approach to Planning</h2>
  <ul class="bullet-list benefits">
    <li>No more paying for man hours, buy a finished product</li>
    <li>Able to focus on getting the right scope, let us focus on your planning</li>
  </ul>
  <div class="corner-mark">DEW</div>
</section>

<!-- Detail planning -->
<section class="slide slide--detail">
  <svg class="slide-frame" viewBox="0 0 559 315" aria-hidden="true">
    <polygon points="0,0 559,0 559,136 524,89 0,89" fill="var(--navy)"/>
    <polygon points="491,0 559,0 559,91" fill="var(--steel)"/>
    <g class="search-network" fill="none" stroke="#1e55e8" stroke-width="6">
      <circle cx="439" cy="38" r="20"/>
      <line x1="424" y1="53" x2="404" y2="73" stroke-width="11" stroke-linecap="round"/>
      <line x1="439" y1="38" x2="489" y2="44"/>
      <line x1="489" y1="44" x2="477" y2="13" stroke-width="3"/>
      <line x1="489" y1="44" x2="477" y2="75" stroke-width="3"/>
    </g>
    <g fill="#1e55e8">
      <circle cx="439" cy="38" r="7"/>
      <circle cx="489" cy="44" r="7"/>
      <circle cx="477" cy="13" r="7"/>
      <circle cx="477" cy="75" r="7"/>
    </g>
  </svg>
  <h2 class="slide-title">Detail Planning</h2>
  <ul class="bullet-list steps-field">
    <li>Conducted field walk &amp; captured field notes</li>
    <li>Collected field photos</li>
    <li>Create job activities, identify resources, estimate durations, identify TA phases</li>
  </ul>
  <ul class="bullet-list steps-office">
    <li>Annotate pictures and P&amp;ID's</li>
    <li>Identify blind points (hydro, &amp; entry blinds)</li>
    <li>Identify PPE requirements</li>
    <li>Provide safety ranking for each activity</li>
    <li>Create material list</li>
    <li>Create job packages</li>
    <li>Capture notes at the activity level</li>
    <li>Scaffold Requirements</li>
  </ul>
  <div class="corner-mark">DEW</div>
</section>

<!-- Flow process -->
<section class="slide slide--flow">
  <svg class="slide-frame" viewBox="0 0 559 315" aria-label="RPS flow process diagram">
    <defs>
      <linearGradient id="orangeBand" x1="0" x2="1">
        <stop offset="0" stop-color="#fbb040"/><stop offset="1" stop-color="#f7941d"/>
      </linearGradient>
    </defs>
    <polygon points="0,50 521,50 559,120 559,315 0,315" fill="var(--navy)"/>

    <!-- top row: on site -->
    <polygon points="92,109 164,109 171,123.5 164,138 92,138" fill="#1fa0e8"/>
    <polygon points="164,109 240,109 247,123.5 240,138 164,138 171,123.5" fill="#1b91e6"/>
    <polygon points="240,109 318,109 325,123.5 318,138 240,138 247,123.5" fill="#1a82e3"/>
    <polygon points="318,109 385,109 392,123.5 385,138 318,138 325,123.5" fill="#1b72e0"/>
    <polygon points="385,109 465,109 465,138 385,138 392,123.5" fill="#1c64dc"/>
    <text class="flow-label flow-label--light" x="132" y="126" text-anchor="middle">Collect Worklist</text>
    <text class="flow-label flow-label--light" x="207" y="126" text-anchor="middle">Scope Review</text>
    <text class="flow-label flow-label--light" x="284" y="126" text-anchor="middle">Planning Premise</text>
    <text class="flow-label flow-label--light" x="355" y="126" text-anchor="middle">Data Collection</text>
    <text class="flow-label flow-label--light" x="421" y="126" text-anchor="middle">Field photos</text>

    <!-- top row icons -->
    <g fill="none" stroke="#2aa6ec" stroke-width="1.4">
      <rect x="126" y="85" width="11" height="15" rx="1"/>
      <line x1="129" y1="89" x2="134" y2="89"/><line x1="129" y1="92" x2="134" y2="92"/><line x1="129" y1="95" x2="134" y2="95"/>
      <circle cx="212" cy="88" r="5"/><circle cx="212" cy="88" r="1.8"/>
      <line x1="208" y1="92" x2="203" y2="98" stroke-width="2.5"/>
      <rect x="265" y="85" width="12" height="15" rx="1"/>
      <line x1="268" y1="89" x2="274" y2="89"/><line x1="268" y1="92" x2="274" y2="92"/><line x1="268" y1="95" x2="274" y2="95"/>
      <rect x="349" y="85" width="13" height="13" rx="1"/>
      <rect x="352" y="85" width="7" height="5"/>
      <rect x="419" y="87" width="16" height="11" rx="2"/><circle cx="427" cy="92.5" r="3"/>
    </g>

    <!-- hubs -->
    <circle cx="65" cy="123" r="30" fill="var(--sky)"/>
    <g fill="#14308f">
      <circle cx="59" cy="106" r="2.6"/><circle cx="71" cy="106" r="2.6"/>
      <path d="M53,117 q6,-9 12,0 z"/><path d="M65,117 q6,-9 12,0 z"/>
      <circle cx="65" cy="112" r="3"/><path d="M58,124 q7,-10 14,0 z"/>
    </g>
    <text class="hub-label" x="65" y="140" text-anchor="middle" fill="#fff">On Site</text>

    <!-- orange row: remote -->
    <path d="M467,140 L494,140 L494,186 Q494,198 482,198 L415,198 L408,183.5 L415,169 L467,169 Z" fill="#f7941d"/>
    <polygon points="300,169 415,169 408,183.5 415,198 300,198 293,183.5" fill="#f89d2a"/>
    <polygon points="205,169 300,169 293,183.5 300,198 205,198 198,183.5" fill="#f9a632"/>
    <path d="M101,169 L205,169 L198,183.5 L205,198 L125,198 L125,220 L110.5,230 L96,220 L96,174 Q96,169 101,169 Z" fill="url(#orangeBand)"/>
    <text class="flow-label flow-label--dark" x="149" y="186" text-anchor="middle">Package Acceptance</text>
    <text class="flow-label flow-label--dark" x="252" y="186" text-anchor="middle">Package Review</text>
    <text class="flow-label flow-label--dark" x="356" y="186" text-anchor="middle">Develope Package</text>
    <text class="flow-label flow-label--dark" x="458" y="186" text-anchor="middle">Detail Planning</text>

    <!-- orange row icons -->
    <g fill="none" stroke="#f7941d" stroke-width="2">
      <polyline points="148,154 153,159 162,149" stroke-width="2.6"/>
      <rect x="229" y="146" width="21" height="12" stroke-width="1.4"/>
      <line x1="232" y1="150" x2="242" y2="150" stroke-width="1.2"/><line x1="232" y1="153" x2="240" y2="153" stroke-width="1.2"/>
      <circle cx="249" cy="155" r="4.5" stroke-width="1.6"/>
      <line x1="252" y1="158" x2="256" y2="162"/>
      <circle cx="353" cy="154" r="4.5" stroke-width="3"/>
      <circle cx="437" cy="153" r="5" stroke-width="1.6"/>
      <line x1="433" y1="157" x2="428" y2="162" stroke-width="2.6"/>
      <line x1="437" y1="153" x2="448" y2="151" stroke-width="1"/>
      <line x1="448" y1="151" x2="445" y2="145" stroke-width="1"/>
      <line x1="448" y1="151" x2="445" y2="158" stroke-width="1"/>
    </g>
    <circle cx="479" cy="123" r="30" fill="#f9a832"/>
    <g fill="#14308f" stroke="#14308f" stroke-width="1">
      <circle cx="467" cy="107" r="2"/><circle cx="492" cy="110" r="2"/><circle cx="479" cy="116" r="2.4"/>
      <line x1="467" y1="107" x2="492" y2="110"/><line x1="469" y1="111" x2="474" y2="116"/>
      <path d="M473,123 q6,-8 12,0 z"/>
    </g>
    <text class="hub-label" x="479" y="140" text-anchor="middle" fill="#14308f">Remote</text>

    <!-- bottom row: levels -->
    <polygon points="96,233 165,233 172,247 165,261 96,261" fill="#f7941d"/>
    <polygon points="165,233 262,233 269,247 262,261 165,261 172,247" fill="#1d7fe2"/>
    <polygon points="262,233 335,233 342,247 335,261 262,261 269,247" fill="#f9a235"/>
    <polygon points="335,233 445,233 445,261 335,261 342,247" fill="#1c8fe6"/>
    <g fill="none" stroke="#14308f" stroke-width="1.3">
      <rect x="102" y="238" width="16" height="15" rx="1.5"/><line x1="102" y1="242" x2="118" y2="242"/>
      <rect x="272" y="238" width="16" height="15" rx="1.5"/><line x1="272" y1="242" x2="288" y2="242"/>
    </g>
    <g fill="#14308f">
      <rect x="105" y="245" width="2.2" height="2.2"/><rect x="109" y="245" width="2.2" height="2.2"/><rect x="113" y="245" width="2.2" height="2.2"/>
      <rect x="105" y="249" width="2.2" height="2.2"/><rect x="109" y="249" width="2.2" height="2.2"/><rect x="113" y="249" width="2.2" height="2.2"/>
      <rect x="275" y="245" width="2.2" height="2.2"/><rect x="279" y="245" width="2.2" height="2.2"/><rect x="283" y="245" width="2.2" height="2.2"/>
      <rect x="275" y="249" width="2.2" height="2.2"/><rect x="279" y="249" width="2.2" height="2.2"/><rect x="283" y="249" width="2.2" height="2.2"/>
    </g>
    <text class="flow-label flow-label--dark" x="134" y="250" text-anchor="middle">Level 1</text>
    <text class="flow-label flow-label--light" x="215" y="250" text-anchor="middle">Schedule Review</text>
    <text class="flow-label flow-label--dark" x="304" y="250" text-anchor="middle">Level 2</text>
    <text class="flow-label flow-label--light" x="386" y="250" text-anchor="middle">Schedule Review</text>

    <g fill="#2aa6ec">
      <circle cx="210" cy="213" r="2"/><circle cx="218" cy="212" r="2"/><circle cx="214" cy="219" r="2.2"/>
      <path d="M204,222 q5,-6 10,0 z"/><path d="M214,222 q5,-6 10,0 z"/><path d="M209,228 q5,-6 10,0 z"/>
      <circle cx="375" cy="213" r="2"/><circle cx="383" cy="212" r="2"/><circle cx="379" cy="219" r="2.2"/>
      <path d="M369,222 q5,-6 10,0 z"/><path d="M379,222 q5,-6 10,0 z"/><path d="M374,228 q5,-6 10,0 z"/>
    </g>

    <circle cx="451" cy="246" r="30" fill="var(--sky)"/>
    <g fill="none" stroke="#14308f" stroke-width="1.4">
      <rect x="443" y="229" width="17" height="15" rx="1.5"/><line x1="443" y1="233" x2="460" y2="233"/>
    </g>
    <g fill="#14308f">
      <rect x="446" y="236" width="2.3" height="2.3"/><rect x="450.3" y="236" width="2.3" height="2.3"/><rect x="454.6" y="236" width="2.3" height="2.3"/>
      <rect x="446" y="240" width="2.3" height="2.3"/><rect x="450.3" y="240" width="2.3" height="2.3"/><rect x="454.6" y="240" width="2.3" height="2.3"/>
    </g>
    <text class="hub-label" x="451" y="258" text-anchor="middle" fill="#fff">Level 3</text>
  </svg>
  <h2 class="slide-title">RPS Flow Process</h2>
  <div class="corner-mark">DEW</div>
</section>

</body>
</html>
```